The Ladder of Mastery Customized for my Business

Hi! I am interested in getting some design ideas to take this Ladder of Mastery and put a bit of branding of my business into it. Open to any and all designs, this is intended to put on a 20"x24" or 16"x20" canvas so I can have it in my office for team training purposes. I have included a picture of the wall this canvas will go on. Thank you!

```html
<!DOCTYPE html>
<html lang="en">
<head>
<meta charset="utf-8">
<title>The Ladder of Mastery</title>
<link href="https://fonts.googleapis.com/css2?family=Montserrat:wght@600;700&family=Poppins:wght@500;600&display=swap" rel="stylesheet">
<style>
  :root {
    --page: #eceff3;
    --blue-deep: #2b3aa3;
    --blue-mid: #2f6fd0;
    --blue-bright: #3fb7ee;
    --frame: #a9def6;
    --slate: #333538;
    --ink: #1d1d1f;
    --white: #ffffff;
  }
  * { box-sizing: border-box; margin: 0; padding: 0; }
  html, body { width: 905px; height: 1200px; overflow: hidden; background: var(--page); }
  .poster {
    position: absolute; left: 0; top: 223px; width: 905px; height: 753px; overflow: hidden;
    background: linear-gradient(170deg, var(--blue-deep) 0%, var(--blue-mid) 45%, var(--blue-bright) 100%);
  }
  .poster::before {
    content: ""; position: absolute; inset: 0;
    background: repeating-linear-gradient(-60deg, rgba(255,255,255,0) 0 34px, rgba(255,255,255,0.08) 34px 52px);
  }
  .pyramid-art { position: absolute; left: 0; top: 0; width: 905px; height: 753px; }
  .title {
    position: absolute; left: 30px; top: 26px;
    font-family: "Montserrat", sans-serif; font-weight: 700; font-size: 48px; line-height: 1.15;
    color: var(--white); text-shadow: 3px 4px 6px rgba(0,0,0,0.35); letter-spacing: -0.5px;
  }
  .brand-seal {
    position: absolute; left: 619px; top: 23px; width: 246px; height: 246px; border-radius: 50%;
    background: var(--white); display: flex; align-items: center; justify-content: center; text-align: center;
  }
  .brand-name {
    font-family: "Poppins", sans-serif; font-weight: 600; font-size: 30px; line-height: 1.1; color: var(--slate);
  }
  .block {
    position: absolute; background: var(--white); text-align: center; padding: 7px 5px 0;
    color: var(--ink); display: flex; flex-direction: column; align-items: center;
  }
  .block-name { font-family: "Montserrat", sans-serif; font-weight: 600; font-size: 14px; line-height: 1.12; letter-spacing: 0.2px; }
  .block-text { font-family: "Poppins", sans-serif; font-weight: 500; font-size: 8.6px; line-height: 1.5; margin-top: 4px; }
  .block-text.airy { line-height: 1.95; margin-top: 6px; }
  .side-label { font-family: "Montserrat", sans-serif; font-weight: 700; fill: var(--white); }
  .side-note { font-family: "Poppins", sans-serif; font-weight: 500; fill: var(--white); }
</style>
</head>
<body>
<main class="poster">
  <svg class="pyramid-art" viewBox="0 0 905 753" aria-hidden="true">
    <defs>
      <clipPath id="inner-pyramid"><polygon points="466,28 70,716 862,716"/></clipPath>
      <linearGradient id="floor" x1="0" y1="0" x2="0" y2="1">
        <stop offset="0" stop-color="#6fd0f5" stop-opacity="0"/>
        <stop offset="1" stop-color="#a8e8fb" stop-opacity="0.55"/>
      </linearGradient>
    </defs>
    <rect x="0" y="700" width="905" height="53" fill="url(#floor)"/>
    <polygon points="466,15 58,723 874,723" fill="var(--frame)"/>
    <g clip-path="url(#inner-pyramid)" fill="var(--slate)">
      <rect x="0" y="28" width="463" height="107"/>
      <rect x="469" y="28" width="436" height="107"/>
      <rect x="0" y="142" width="394" height="107"/>
      <rect x="538" y="142" width="367" height="107"/>
      <rect x="0" y="259" width="330" height="107"/>
      <rect x="602" y="259" width="303" height="107"/>
      <rect x="0" y="375" width="260" height="109"/>
      <rect x="672" y="375" width="233" height="109"/>
      <rect x="0" y="491" width="195" height="107"/>
      <rect x="737" y="491" width="168" height="107"/>
      <rect x="0" y="608" width="128" height="108"/>
      <rect x="804" y="608" width="101" height="108"/>
    </g>
    <g text-anchor="middle">
      <g transform="translate(444,106) rotate(-60)"><text class="side-label" font-size="9">TRUST</text><text class="side-note" y="8" font-size="5.5">(in the mission)</text></g>
      <g transform="translate(488,106) rotate(60)"><text class="side-label" font-size="9">CALM</text><text class="side-note" y="8" font-size="5.5">(results take time)</text></g>
      <g transform="translate(374,222) rotate(-60)"><text class="side-label" font-size="9">GRIT</text><text class="side-note" y="8" font-size="5.5">(steady effort)</text></g>
      <g transform="translate(558,222) rotate(60)"><text class="side-label" font-size="9">HONOR</text><text class="side-note" y="8" font-size="5.5">(clear motives)</text></g>
      <g transform="translate(307,336) rotate(-60)"><text class="side-label" font-size="9">CREATIVITY</text><text class="side-note" y="8" font-size="5.5">(sound choices)</text></g>
      <g transform="translate(625,336) rotate(60)"><text class="side-label" font-size="9">DEPENDABILITY</text><text class="side-note" y="8" font-size="5.5">(earns trust)</text></g>
      <g transform="translate(238,454) rotate(-60)"><text class="side-label" font-size="9">FLEXIBILITY</text><text class="side-note" y="8" font-size="5.5">(in any setting)</text></g>
      <g transform="translate(694,454) rotate(60)"><text class="side-label" font-size="9">TRUTH</text><text class="side-note" y="8" font-size="5.5">(in word and deed)</text></g>
      <g transform="translate(173,568) rotate(-60)"><text class="side-label" font-size="9">DRIVE</text><text class="side-note" y="8" font-size="5.5">(for worthy goals)</text></g>
      <g transform="translate(759,568) rotate(60)"><text class="side-label" font-size="9">GENUINENESS</text><text class="side-note" y="8" font-size="5.5">(builds bonds)</text></g>
    </g>
  </svg>

  <h1 class="title">THE LADDER<br>OF MASTERY</h1>

  <div class="brand-seal"><span class="brand-name">Harbor Point<br>Health</span></div>

  <section class="block" style="left:399px;top:142px;width:124px;height:107px;">
    <h2 class="block-name">PEAK<br>PERFORMANCE</h2>
    <p class="block-text">Rise to your best when it counts most. Welcome the hard moments.</p>
  </section>

  <section class="block" style="left:335px;top:259px;width:126px;height:107px;">
    <h2 class="block-name">COMPOSURE</h2>
    <p class="block-text">Stay true to who you are. Remain steady in every setting. Stay calm under pressure.</p>
  </section>
  <section class="block" style="left:470px;top:259px;width:126px;height:107px;">
    <h2 class="block-name">SELF-BELIEF</h2>
    <p class="block-text airy">Trust built through effort. It grows from careful preparation.</p>
  </section>

  <section class="block" style="left:265px;top:375px;width:125px;height:109px;">
    <h2 class="block-name">WELLNESS</h2>
    <p class="block-text">Body, mind and character. Sleep, movement and nutrition matter. Balance every habit. Cut out what drains you.</p>
  </section>
  <section class="block" style="left:399px;top:375px;width:124px;height:109px;">
    <h2 class="block-name">CRAFT</h2>
    <p class="block-text airy">Master the basics and deliver them with precision and speed every day.</p>
  </section>
  <section class="block" style="left:532px;top:375px;width:125px;height:109px;">
    <h2 class="block-name">UNITY</h2>
    <p class="block-text">Put the group before yourself. Share credit freely and work for the good of the whole team.</p>
  </section>

  <section class="block" style="left:200px;top:491px;width:126px;height:107px;">
    <h2 class="block-name">DISCIPLINE</h2>
    <p class="block-text" style="line-height:1.7">Hold steady habits and manage your reactions. Sound thinking and practical sense matter.</p>
  </section>
  <section class="block" style="left:335px;top:491px;width:126px;height:107px;">
    <h2 class="block-name">AWARENESS</h2>
    <p class="block-text" style="line-height:1.8">Notice everything around you. Keep an open mind. Stay hungry to grow.</p>
  </section>
  <section class="block" style="left:470px;top:491px;width:126px;height:107px;">
    <h2 class="block-name">INITIATIVE</h2>
    <p class="block-text" style="line-height:1.7">Make decisions with courage and think for yourself. Treat mistakes as lessons, not setbacks.</p>
  </section>
  <section class="block" style="left:605px;top:491px;width:126px;height:107px;">
    <h2 class="block-name">FOCUS</h2>
    <p class="block-text">Choose a clear target. Commit to reaching it, ignore distractions and keep pushing forward with resolve.</p>
  </section>

  <section class="block" style="left:133px;top:608px;width:123px;height:108px;">
    <h2 class="block-name">DILIGENCE</h2>
    <p class="block-text airy">Nothing replaces effort. Lasting results grow from steady, careful work.</p>
  </section>
  <section class="block" style="left:265px;top:608px;width:124px;height:108px;">
    <h2 class="block-name">RAPPORT</h2>
    <p class="block-text">Built on shared trust, respect and care. Like any bond it needs attention and effort from both sides.</p>
  </section>
  <section class="block" style="left:399px;top:608px;width:124px;height:108px;">
    <h2 class="block-name">COMMITMENT</h2>
    <p class="block-text airy">To your own values and to everyone who relies on you. Keep your word.</p>
  </section>
  <section class="block" style="left:532px;top:608px;width:125px;height:108px;">
    <h2 class="block-name">TEAMWORK</h2>
    <p class="block-text">Across every role in the clinic. Listen first so others will listen. Seek the best answer, not the one that is yours.</p>
  </section>
  <section class="block" style="left:666px;top:608px;width:125px;height:108px;">
    <h2 class="block-name">ENERGY</h2>
    <p class="block-text airy">Spreads to everyone you meet each day. Truly love the work you do.</p>
  </section>
</main>
</body>
</html>
```